Journeys With Marcella Business Cards

I need a business card design for my upscale Travel Agency.
Attached you can find my logo.
I would like to include the following:
- Name
- Title
- Phone Number
- Email
- Website
- and then something like: Follow us: JourneysWithMarcella (and then social media icons in color).
The logo should be in the front and then also the back.
I am also attaching a design that I liked (mostly for the layout) but open to any suggestions
Industry/Entity Type
Travel Agent
Contact Information for Business Card
Name: Marcella Dorn
Title: Travel Designer / Owner
Phone: 415-927-3308
Email: marcella@journeyswithmarcella-example.com
Website: www.JourneysWithMarcella-example.com
Social Media Handles for FB,IG, Twitter: JourneysWithMarcella
Colors
Designer to choose colors to be used in the design.
Look and feel

```html
<!DOCTYPE html>
<html lang="en">
<head>
<meta charset="utf-8">
<title>Journeys With Marcella — Business Cards</title>
<link rel="stylesheet" href="https://fonts.googleapis.com/css2?family=Mulish:wght@400;500;800&family=Patrick+Hand&display=swap">
<style>
  :root {
    --backdrop: #d6d6d6;
    --card: #ffffff;
    --accent: #f5a95a;
    --accent-soft: #f8c592;
    --ink: #3b3b3b;
  }
  * { box-sizing: border-box; margin: 0; padding: 0; }
  html, body {
    width: 1125px;
    height: 1200px;
    overflow: hidden;
  }
  body {
    background: var(--backdrop);
    font-family: "Mulish", sans-serif;
    color: var(--ink);
    position: relative;
  }
  .card {
    position: absolute;
    left: 178px;
    width: 770px;
    height: 438px;
    background: var(--card);
    border-radius: 26px;
  }
  .card--front { top: 140px; }
  .card--back { top: 627px; }

  .brand {
    position: absolute;
    display: flex;
    align-items: center;
    color: var(--accent);
    font-weight: 800;
    white-space: nowrap;
  }
  .brand__mark {
    background: var(--accent);
    flex: none;
  }
  .card--front .brand {
    left: 50px;
    top: 200px;
    font-size: 20px;
    gap: 12px;
  }
  .card--front .brand__mark { width: 30px; height: 30px; }

  .divider {
    position: absolute;
    left: 385px;
    top: 130px;
    width: 1.5px;
    height: 176px;
    background: linear-gradient(to bottom, transparent, var(--accent-soft) 20%, var(--accent-soft) 80%, transparent);
  }
  .contact {
    position: absolute;
    left: 413px;
    top: 126px;
  }
  .contact__name {
    color: var(--accent);
    font-weight: 800;
    font-size: 27px;
    letter-spacing: 1.5px;
    text-transform: uppercase;
    line-height: 1;
  }
  .contact__title {
    margin-top: 12px;
    font-size: 17px;
    font-weight: 500;
  }
  .contact__list {
    list-style: none;
    margin-top: 22px;
  }
  .contact__item {
    display: flex;
    align-items: center;
    gap: 9px;
    font-size: 15px;
    font-weight: 500;
    height: 26.5px;
  }
  .icon { width: 16px; height: 16px; flex: none; }
  .social-dot {
    width: 16px; height: 16px;
    border-radius: 50%;
    background: var(--accent);
    flex: none;
  }

  .card--back .brand {
    left: 50%;
    top: 182px;
    transform: translateX(-50%);
    font-size: 34px;
    gap: 18px;
  }
  .card--back .brand__mark { width: 52px; height: 52px; }
  .back-url {
    position: absolute;
    left: 0;
    right: 0;
    top: 380px;
    text-align: center;
    font-family: "Patrick Hand", cursive;
    font-size: 21px;
    letter-spacing: 1px;
    color: var(--ink);
  }
  .back-url__domain { color: var(--accent); }
</style>
</head>
<body>
  <section class="card card--front" aria-label="Business card front">
    <div class="brand">
      <span class="brand__mark"></span>
      <span class="brand__name">Journeys With Marcella</span>
    </div>
    <div class="divider"></div>
    <div class="contact">
      <h1 class="contact__name">Marcella Dorn</h1>
      <p class="contact__title">Travel Designer / Owner</p>
      <ul class="contact__list">
        <li class="contact__item">
          <svg class="icon" viewBox="0 0 16 16" aria-hidden="true">
            <circle cx="8" cy="8" r="8" fill="var(--accent)"/>
            <path d="M5.2 4.2l1.6-.4.9 2-1 .8c.5 1.1 1.3 1.9 2.4 2.4l.8-1 2 .9-.4 1.6c-3.5.2-6.5-2.8-6.3-6.3z" fill="#fff"/>
          </svg>
          <span>415-927-3308</span>
        </li>
        <li class="contact__item">
          <svg class="icon" viewBox="0 0 16 16" aria-hidden="true">
            <circle cx="8" cy="8" r="8" fill="var(--accent)"/>
            <rect x="4" y="5.2" width="8" height="5.6" fill="none" stroke="#fff" stroke-width="1.1"/>
            <path d="M4 5.4l4 3 4-3" fill="none" stroke="#fff" stroke-width="1.1"/>
          </svg>
          <span>marcella@journeyswithmarcella-example.com</span>
        </li>
        <li class="contact__item">
          <svg class="icon" viewBox="0 0 16 16" aria-hidden="true">
            <circle cx="8" cy="8" r="8" fill="var(--accent)"/>
            <circle cx="8" cy="8" r="4.2" fill="none" stroke="#fff" stroke-width="1.1"/>
            <path d="M3.8 8h8.4M8 3.8c-1.6 2.4-1.6 6 0 8.4M8 3.8c1.6 2.4 1.6 6 0 8.4" fill="none" stroke="#fff" stroke-width="0.9"/>
          </svg>
          <span>www.JourneysWithMarcella-example.com</span>
        </li>
        <li class="contact__item">
          <span class="social-dot"></span>
          <span>JourneysWithMarcella</span>
        </li>
      </ul>
    </div>
  </section>

  <section class="card card--back" aria-label="Business card back">
    <div class="brand">
      <span class="brand__mark"></span>
      <span class="brand__name">Journeys With Marcella</span>
    </div>
    <p class="back-url">www.<span class="back-url__domain">JourneysWithMarcella-example</span>.com</p>
  </section>
</body>
</html>
```